Letterhead and business cards for criminal defense law firm
with existing logo
Letterhead and business cards for criminal defense law firm - Law
Creative Brief
Simple
The Law Office of Marcus Varek, PLLC
718 Birchwood Avenue, Suite 300 Houston, TX 77019
Varek@BrightCounselGroup.net
I would like to incorporate our slogan: Experienced criminal defense lawyers Or if you think of a better slogan/motto, feel free to incorporate it. I am not a flashy or showy lawyer. I want the card to invoke credibility, stability and intelligence (not an ambulance chaser or sleazy lawyer).

```html
<!DOCTYPE html>
<html lang="en">
<head>
<meta charset="UTF-8">
<title>Marcus Varek, PLLC – Business Card</title>
<link rel="stylesheet" href="https://fonts.googleapis.com/css2?family=Montserrat:wght@400;600;700&family=Open+Sans:wght@400;600&display=swap">
<style>
  :root {
    --navy: #262a44;
    --ink: #3a3d52;
    --paper: #ffffff;
    --backdrop: #e9e7e3;
  }
  * { margin: 0; padding: 0; box-sizing: border-box; }
  html, body {
    width: 1200px;
    height: 914px;
    overflow: hidden;
    background: var(--backdrop);
  }
  .canvas {
    position: relative;
    width: 1200px;
    height: 914px;
  }
  .business-card {
    position: absolute;
    left: 100px;
    top: 171px;
    width: 1000px;
    height: 572px;
    background: var(--paper);
    box-shadow: 0 10px 30px rgba(0,0,0,0.12);
  }
  .firm-mark {
    position: absolute;
    left: 230px;
    top: 70px;
    display: flex;
    align-items: center;
    gap: 16px;
  }
  .firm-mark__square {
    width: 104px;
    height: 104px;
    background: var(--navy);
    flex: none;
  }
  .firm-mark__name {
    font-family: "Montserrat", sans-serif;
    font-weight: 600;
    color: var(--navy);
    display: flex;
    flex-direction: column;
    line-height: 1;
  }
  .firm-mark__prefix {
    font-size: 15px;
    letter-spacing: 3px;
    margin-bottom: 6px;
  }
  .firm-mark__title {
    font-size: 58px;
    letter-spacing: 1px;
  }
  .firm-mark__suffix {
    font-size: 15px;
    letter-spacing: 3px;
    align-self: flex-end;
    margin-top: 6px;
  }
  .contact-band {
    position: absolute;
    left: 120px;
    top: 215px;
    width: 44px;
    height: 200px;
    background: var(--navy);
    display: flex;
    flex-direction: column;
    align-items: center;
    justify-content: center;
    gap: 17px;
  }
  .contact-band__dot {
    width: 14px;
    height: 14px;
    border-radius: 50%;
    background: var(--paper);
  }
  .contact-list {
    position: absolute;
    left: 182px;
    top: 232px;
    list-style: none;
    font-family: "Open Sans", sans-serif;
    font-size: 15px;
    line-height: 24px;
    color: var(--ink);
  }
  .card-holder {
    position: absolute;
    right: 60px;
    bottom: 52px;
    font-family: "Open Sans", sans-serif;
    font-weight: 600;
    font-size: 34px;
    color: var(--navy);
  }
</style>
</head>
<body>
<div class="canvas">
  <div class="business-card">
    <div class="firm-mark">
      <div class="firm-mark__square"></div>
      <div class="firm-mark__name">
        <span class="firm-mark__prefix">THE LAW OFFICE OF</span>
        <span class="firm-mark__title">MARCUS VAREK</span>
        <span class="firm-mark__suffix">PLLC</span>
      </div>
    </div>

    <div class="contact-band">
      <span class="contact-band__dot"></span>
      <span class="contact-band__dot"></span>
      <span class="contact-band__dot"></span>
      <span class="contact-band__dot"></span>
      <span class="contact-band__dot"></span>
    </div>

    <ul class="contact-list">
      <li>718 Birchwood Avenue, Suite 300</li>
      <li>Houston, TX 77019</li>
      <li>713-555-0142</li>
      <li>713-555-0187</li>
      <li>Varek@BrightCounselGroup.net</li>
      <li>www.BrightCounselGroup.net</li>
    </ul>

    <div class="card-holder">Daniel Hartwell</div>
  </div>
</div>
</body>
</html>
```